Weight Loss Banner Ad

We need banner ads for our website, www.brightplatekitchen.com. We would like to see Banner ads that represent what you think is the most captivating aspect of The MealWise Plan. Please review the website.

The banner ad should be something you REALLY want to click on. It needs to include the name and/or logo and the slogan "Gourmet Meals Direct To Your House"

We will want the final ad in multiple sizes but it should use the same image and copy.

Logo is attached, so are images. Feel free to use your own if you think you have a better on

Size (pixels):
468 x 60
392 x 72
234 x 60
125 x 125
120 x 90
120 x 60
88 x 31
120 x 240
120 x 600
160 x 600

Target Market(s)

Fitness Enthusiast looking to lose weight.

Industry/Entity Type

Weight

Font styles to use
Sans Serif

Requirements
Must have
• See Description
Nice to have
• Should be awesome and make you want to buy some food. Also you may want to say something about the price:

i.e. Starting at only $99

```html
<!DOCTYPE html>
<html lang="en">
<head>
<meta charset="utf-8">
<title>The MealWise Plan – Skyscraper Banner</title>
<link href="https://fonts.googleapis.com/css2?family=Ubuntu:wght@300;500;700&display=swap" rel="stylesheet">
<style>
  :root {
    --page-bg: #e9e6e1;
    --green-top: #93c623;
    --green-mid: #7cb01c;
    --green-bottom: #5c8f12;
    --green-dark: #2f4a0c;
    --white: #ffffff;
    --button-top: #ffe04a;
    --button-bottom: #f4b400;
    --button-text: #2a2a1a;
    --photo-light: #e4e1dc;
    --photo-mid: #cdb8a6;
    --photo-dark: #8a6a55;
  }
  * { margin: 0; padding: 0; box-sizing: border-box; }
  html, body {
    width: 1200px; height: 990px; overflow: hidden;
    background: var(--page-bg);
    font-family: "Ubuntu", sans-serif;
  }
  .banner {
    position: absolute; left: 480px; top: 45px;
    width: 240px; height: 900px; overflow: hidden;
    background: linear-gradient(180deg, var(--green-top) 0%, var(--green-mid) 55%, var(--green-bottom) 100%);
    box-shadow: 0 4px 14px rgba(0,0,0,.25);
  }
  .brand {
    position: absolute; left: 0; top: 18px; width: 240px;
    text-align: center; color: var(--white);
    font-weight: 700; font-size: 30px; line-height: 1.05; letter-spacing: -0.5px;
  }
  .slogan {
    position: absolute; left: 12px; top: 88px; width: 216px;
    text-align: center; color: var(--white);
    font-weight: 500; font-size: 14px; line-height: 1.2;
  }
  .hero-photo { position: absolute; left: 0; top: 138px; width: 240px; height: 340px; }
  .copy { position: absolute; left: 0; width: 240px; line-height: 1; }
  .copy-lead { top: 494px; left: 16px; color: var(--white); font-weight: 300; font-size: 30px; }
  .copy-line { color: var(--green-dark); font-weight: 700; font-size: 44px; text-align: center; }
  .copy-easiest { top: 526px; }
  .copy-way { top: 572px; }
  .copy-punch { top: 628px; color: var(--white); font-weight: 700; font-size: 56px; text-align: center; letter-spacing: -1px; }
  .price-label { top: 700px; left: 70px; color: var(--white); font-weight: 300; font-size: 26px; }
  .price { top: 730px; color: var(--white); font-weight: 700; font-size: 74px; text-align: center; letter-spacing: -1px; }
  .pointer { position: absolute; left: 111px; top: 812px; }
  .cta {
    position: absolute; left: 22px; top: 838px; width: 196px; height: 44px;
    border-radius: 22px;
    background: linear-gradient(180deg, var(--button-top), var(--button-bottom));
    box-shadow: 0 2px 4px rgba(0,0,0,.3);
    color: var(--button-text); font-weight: 700; font-size: 22px;
    display: flex; align-items: center; justify-content: center;
  }
</style>
</head>
<body>
  <div class="banner">
    <div class="brand">The MealWise<br>Plan</div>
    <div class="slogan">Gourmet Meals Direct<br>To Your House</div>

    <svg class="hero-photo" viewBox="0 0 240 340" role="img" aria-label="Photo of a woman eating a fresh salad with a fork">
      <defs>
        <linearGradient id="photoTone" x1="0" y1="0" x2="0" y2="1">
          <stop offset="0" stop-color="var(--photo-light)"/>
          <stop offset="0.55" stop-color="var(--photo-mid)"/>
          <stop offset="1" stop-color="var(--photo-dark)"/>
        </linearGradient>
      </defs>
      <path d="M0 20 Q120 -4 240 20 L240 312 Q120 336 0 318 Z" fill="url(#photoTone)"/>
      <path d="M0 20 Q120 -4 240 20" fill="none" stroke="var(--white)" stroke-width="5"/>
      <path d="M0 318 Q120 336 240 312" fill="none" stroke="var(--white)" stroke-width="5"/>
    </svg>

    <div class="copy copy-lead">the</div>
    <div class="copy copy-line copy-easiest">easiest</div>
    <div class="copy copy-line copy-way">way to</div>
    <div class="copy copy-punch">eat well!</div>
    <div class="copy price-label">only</div>
    <div class="copy price">$99!</div>

    <svg class="pointer" width="18" height="9" viewBox="0 0 18 9" aria-hidden="true">
      <path d="M0 0 H18 L9 9 Z" fill="var(--green-dark)"/>
    </svg>

    <div class="cta">START NOW!</div>
  </div>
</body>
</html>
```